Clay Sparrow- Hand made fashion accessories

Clay sparrow is a new business that will be selling hand made fashion accessories for women such as bags, baskets, knecklaces etc. The items are all hand made from Africa. I would like natural colors leaning more to the cardboard rustic look. I would like the card to look simple but elegant at the same time.

Industry/Entity Type

Business

Contact Information for Business Card

www.claysparrow-example.com.au
sales@claysparrow-example.com.au
Tel: 0452867310

Font styles to use
Decorative
Script

Requirements
Must have
• Earthy and rustic colours. Straw, cardboard etc. Fine black cursive print. One side of card only name
• second side website, email and tel.
Should not have
• No need to have any description of what business sells or does. No pictures of anything.

```html
<!DOCTYPE html>
<html lang="en">
<head>
<meta charset="utf-8">
<title>Clay Sparrow – Business Card</title>
<link rel="stylesheet" href="https://fonts.googleapis.com/css2?family=Great+Vibes&family=Cormorant+Garamond:wght@400&display=swap">
<style>
  :root {
    --backdrop: #e8e2d6;
    --card: #f4efe4;
    --band: #c49a66;
    --band-edge: #a97f4e;
    --ink: #1a1612;
  }
  * { margin: 0; padding: 0; box-sizing: border-box; }
  html, body {
    width: 1200px;
    height: 892px;
    overflow: hidden;
    background: var(--backdrop);
  }
  .canvas {
    position: relative;
    width: 1200px;
    height: 892px;
  }
  .card {
    position: absolute;
    background: var(--card);
    box-shadow: 0 6px 18px rgba(60, 40, 20, 0.18);
    overflow: hidden;
  }
  .card--front {
    left: 90px;
    top: 290px;
    width: 560px;
    height: 320px;
  }
  .card--back {
    left: 770px;
    top: 166px;
    width: 320px;
    height: 560px;
  }
  .band {
    position: absolute;
    left: 0;
    width: 100%;
    background: var(--band);
    border-top: 1px solid var(--band-edge);
    border-bottom: 1px solid var(--band-edge);
    display: flex;
    align-items: center;
    justify-content: center;
    white-space: nowrap;
  }
  .brand-name {
    font-family: "Great Vibes", cursive;
    font-weight: 400;
    color: var(--ink);
    line-height: 1;
  }
  .card--front .band {
    top: 200px;
    height: 120px;
    border-bottom: none;
  }
  .card--front .brand-name {
    font-size: 62px;
  }
  .card--back .band {
    top: 350px;
    height: 86px;
  }
  .card--back .brand-name {
    font-size: 46px;
  }
  .contact {
    position: absolute;
    left: 0;
    width: 100%;
    top: 146px;
    text-align: center;
    color: var(--ink);
    font-family: "Cormorant Garamond", serif;
    font-style: normal;
    font-size: 15px;
    line-height: 1.35;
  }
</style>
</head>
<body>
  <main class="canvas">
    <section class="card card--front" aria-label="Card front">
      <div class="band">
        <span class="brand-name">Clay Sparrow</span>
      </div>
    </section>

    <section class="card card--back" aria-label="Card back">
      <address class="contact">
        <div class="contact__phone">0452867310</div>
        <div class="contact__email">sales@claysparrow-example.com.au</div>
        <div class="contact__web">www.claysparrow-example.com.au</div>
      </address>
      <div class="band">
        <span class="brand-name">Clay Sparrow</span>
      </div>
    </section>
  </main>
</body>
</html>
```